Kelvar Systems Website

Website design for our company: Kelvar Systems.
The website should look fresh and IT focused. Please have a look at http://www.kelvarsystems.net.au/ for our current design. We want something fresh and new, professional looking, in WordPress so we can easily make changes.

Industry/Entity Type

It Company

```html
<!DOCTYPE html>
<html lang="en">
<head>
<meta charset="utf-8">
<title>Kelvar Systems</title>
<link rel="stylesheet" href="https://fonts.googleapis.com/css2?family=Questrial&family=Open+Sans:wght@400;600;700&display=swap">
<style>
:root{
  --blue:#0f6fb8;
  --blue-dark:#0b4f86;
  --blue-nav:#1a76c2;
  --green:#0aa84f;
  --green-dark:#078a3f;
  --text:#444;
  --heading:#0f6fb8;
  --gray-bg:#f3f3f3;
  --line:#dcdcdc;
  --white:#fff;
  --footer:#0d6cb6;
  --footer-bar:#0a4f86;
  --logo-gray:#9a9a9a;
}
*{margin:0;padding:0;box-sizing:border-box}
html,body{width:1200px;height:2311px;overflow:hidden}
body{position:relative;background:var(--white);font-family:"Open Sans",sans-serif;color:var(--text)}
.abs{position:absolute}
.top-rule{left:0;top:0;width:1200px;height:3px;background:var(--blue)}
.brand{left:51px;top:34px;width:219px;height:112px;display:flex;align-items:center;gap:12px}
.brand-mark{width:22px;height:22px;background:var(--green)}
.brand-name{font-family:"Questrial",sans-serif;font-size:28px;color:var(--green);line-height:1}
.call{right:48px;top:54px;text-align:right;font-family:"Questrial",sans-serif;color:var(--green);font-size:18px}
.call .num{display:block;color:var(--blue);font-size:18px;letter-spacing:1px;margin-top:4px}
.social{right:48px;top:117px;display:flex;gap:7px}
.social span{width:26px;height:26px;border-radius:50%;background:var(--blue)}
.social span:last-child{background:#e58a1c}
.hero{left:0;top:193px;width:1200px;height:503px;background:linear-gradient(#f4f4f4,#e3e3e3 70%,#d6d6d6)}
.nav{left:48px;top:177px;width:1104px;height:43px;background:linear-gradient(#2a86d0,var(--blue-nav) 50%,#1364aa);border-radius:3px;box-shadow:0 3px 5px rgba(0,0,0,.25);display:flex;align-items:center;padding-left:10px}
.nav a{color:var(--white);text-decoration:none;font-size:14px;letter-spacing:.5px;padding:0 22px;border-right:1px solid rgba(255,255,255,.25);line-height:26px}
.nav a:last-of-type{border-right:none}
.search{position:absolute;right:14px;top:8px;width:186px;height:27px;background:var(--white);border-radius:2px;font-size:12px;color:#999;padding:6px 8px}
.search svg{position:absolute;right:8px;top:7px}
.hero-title{left:69px;top:294px;font-family:"Questrial",sans-serif;font-size:28px;line-height:33px;color:var(--heading);letter-spacing:1.5px}
.hero-text{left:72px;width:548px;font-size:16px;line-height:22px;color:#555}
.btn{display:flex;align-items:center;justify-content:center;gap:12px;color:var(--white);font-size:16px;border-radius:3px}
.btn i{width:22px;height:22px;border-radius:50%;background:var(--white);display:flex;align-items:center;justify-content:center}
.btn-green{left:72px;top:534px;width:150px;height:40px;background:linear-gradient(#16b95d,var(--green-dark))}
.btn-blue{left:239px;top:534px;width:149px;height:40px;background:linear-gradient(#2a86d0,#125fa2)}
.hero-media{left:661px;top:297px;width:440px;height:350px;border-radius:8px;background:linear-gradient(#2a2a2a 0 73%,#d8d8d8 73% 86%,#c4c4c4 86%)}
.services{left:0;top:696px;width:1200px;height:593px;background:var(--gray-bg)}
.sec-title{font-family:"Questrial",sans-serif;font-size:17px;letter-spacing:1px;color:var(--heading)}
.sec-title b{font-weight:400;color:var(--green)}
.rule{height:1px;background:var(--line)}
.dots{left:1068px;top:786px;display:flex;gap:5px}
.dots span{width:10px;height:10px;border-radius:50%;background:var(--blue)}
.dots span:first-child{background:var(--green)}
.card{top:838px;width:329px;height:381px;text-align:center}
.card.active{background:linear-gradient(#fff,#ececec);border:1px solid #d8d8d8;border-top:4px solid var(--green)}
.card svg{margin-top:28px}
.card h3{font-family:"Questrial",sans-serif;font-weight:400;font-size:17px;color:var(--heading);letter-spacing:.5px;margin-top:38px}
.card p{font-size:13.5px;line-height:19px;color:#555;margin:12px auto 0;width:300px}
.card .more{display:inline-block;margin-top:10px;width:90px;height:28px;line-height:28px;background:var(--green);color:var(--white);font-size:12px}
.welcome-photo{left:62px;top:1391px;width:385px;height:288px;background:linear-gradient(#f3f3f3,#e6e9ee)}
.welcome-text{left:476px;top:1410px;width:640px;font-size:16.5px;line-height:22px;color:#555}
.welcome-text p{margin-bottom:22px}
.partners{left:0;top:1679px;width:1200px;height:164px;background:#ececec;display:flex;align-items:center;justify-content:space-around;padding:0 100px}
.partners span{font-family:"Open Sans",sans-serif;font-weight:700;font-size:30px;color:var(--logo-gray)}
.footer{left:0;top:1843px;width:1200px;height:424px;background:var(--footer);color:var(--white)}
.f-head{font-family:"Questrial",sans-serif;font-size:16px;letter-spacing:1px}
.f-rule{height:1px;background:rgba(255,255,255,.3)}
.event-thumb{width:131px;height:89px;border:3px solid #5aa0d8;background:linear-gradient(135deg,#e8eef5,#b9c8d8)}
.event{left:246px;width:260px;font-size:14px;line-height:17px}
.event h4{font-size:14.5px;font-weight:700;letter-spacing:.5px;margin-bottom:4px}
.event .rm{display:block;margin-top:8px;letter-spacing:.5px}
.links{left:588px;top:1958px;list-style:none;font-size:15px;line-height:30.5px}
.links li::before{content:"›";margin-right:10px}
.msg-intro{left:873px;top:1962px;font-size:14.5px;line-height:18px}
.field{left:873px;width:234px;background:#0c4f8a;border:1px solid #2b76b5;border-radius:2px;font-size:13px;padding:6px 10px}
.submit{left:875px;top:2176px;width:91px;height:32px;background:var(--green);font-size:14px;display:flex;align-items:center;justify-content:center;border-radius:2px}
.bar{left:0;top:2267px;width:1200px;height:44px;background:var(--footer-bar);color:var(--white);font-size:13px}
.bar-links{left:98px;top:13px;letter-spacing:.5px;word-spacing:6px}
.bar-copy{left:475px;top:13px}
.bar-social{right:190px;top:9px;display:flex;gap:8px}
.bar-social span{width:26px;height:26px;border-radius:50%;background:var(--white)}
</style>
</head>
<body>
<div class="abs top-rule"></div>
<div class="abs hero"></div>

<header>
  <div class="abs brand"><span class="brand-mark"></span><span class="brand-name">Kelvar Systems</span></div>
  <div class="abs call">
    <svg width="14" height="14" viewBox="0 0 24 24"><path fill="#0aa84f" d="M6.6 10.8a15 15 0 006.6 6.6l2.2-2.2c.3-.3.7-.4 1-.2 1.1.4 2.3.6 3.6.6.6 0 1 .4 1 1V20c0 .6-.4 1-1 1A17 17 0 013 4c0-.6.4-1 1-1h3.5c.6 0 1 .4 1 1 0 1.3.2 2.5.6 3.6.1.3 0 .7-.2 1z"/></svg>
    Call us:<span class="num">555-014-2290</span>
  </div>
  <div class="abs social"><span></span><span></span><span></span><span></span></div>
  <nav class="abs nav">
    <a>HOME</a><a>ABOUT US</a><a>SERVICES</a><a>CLIENTS</a><a>SUPPORTS</a><a>TESTIMONIALS</a><a>CONTACT US</a>
    <div class="search">Keyword Search<svg width="12" height="12" viewBox="0 0 12 12"><circle cx="5" cy="5" r="3.5" fill="none" stroke="#888" stroke-width="1.5"/><path d="M7.5 7.5L11 11" stroke="#888" stroke-width="1.5"/></svg></div>
  </nav>
</header>

<section>
  <h1 class="abs hero-title" style="font-weight:400">TO EXCEL IN SUPPORT AND SERVICE<br>OF ALL COMPUTER AND IT NEEDS.</h1>
  <p class="abs hero-text" style="top:374px">Lorem ipsum dolor sit amet, consectetur adipiscing elit. Phasellus eget leo leo. Sed adipiscing mi orci, vel ultrices turpis mattis a. Quisque sed eros luctus, euismod ligula et, suscipit dolor.</p>
  <p class="abs hero-text" style="top:463px">Sed adipiscing mi orci, vel ultrices turpis mattis a. Quisque sed eros luctus, euismod ligula et, suscipit dolor ipsum dolor sit amet.</p>
  <a class="abs btn btn-green">Read more <i><svg width="12" height="12" viewBox="0 0 12 12"><path d="M1 6h9M6 2l4 4-4 4" fill="none" stroke="#0aa84f" stroke-width="2"/></svg></i></a>
  <a class="abs btn btn-blue">Contact us <i><svg width="12" height="12" viewBox="0 0 24 24"><path fill="#1a76c2" d="M6.6 10.8a15 15 0 006.6 6.6l2.2-2.2c.3-.3.7-.4 1-.2 1.1.4 2.3.6 3.6.6.6 0 1 .4 1 1V20c0 .6-.4 1-1 1A17 17 0 013 4c0-.6.4-1 1-1h3.5c.6 0 1 .4 1 1 0 1.3.2 2.5.6 3.6.1.3 0 .7-.2 1z"/></svg></i></a>
  <div class="abs hero-media" role="img" aria-label="Desktop monitor showing a businessman standing in a bright office"></div>
</section>

<section>
  <div class="abs services"></div>
  <h2 class="abs sec-title" style="left:83px;top:775px;font-weight:400">OUR SERVICES</h2>
  <div class="abs dots"><span></span><span></span><span></span></div>
  <div class="abs rule" style="left:83px;top:808px;width:1034px"></div>

  <div class="abs card" style="left:47px">
    <svg width="140" height="114" viewBox="0 0 140 114"><g stroke="#1a76c2" stroke-width="3" fill="#1a76c2"><path d="M74 62L46 28M74 62L88 24M74 62L130 30M74 62L118 70M74 62L24 52M74 62L36 90M74 62L82 108M74 62L116 96M46 28L14 44M88 24L46 28"/><circle cx="74" cy="62" r="24"/><circle cx="46" cy="28" r="13"/><circle cx="88" cy="24" r="8"/><circle cx="130" cy="30" r="8"/><circle cx="118" cy="70" r="7"/><circle cx="14" cy="44" r="6"/><circle cx="24" cy="52" r="5"/><circle cx="36" cy="90" r="9"/><circle cx="82" cy="108" r="5"/><circle cx="116" cy="96" r="9"/></g></svg>
    <h3>Network related services</h3>
    <p>Lorem ipsum dolor sit amet, consectetur adipiscing elit. Curabitur lacinia pretium risus ac euismod.Arabitur lorem lacinia pretium risus ac ipsum dolor sit amet consectetur adi.</p>
    <span class="more">read more</span>
  </div>

  <div class="abs card active" style="left:433px">
    <svg width="120" height="104" viewBox="0 0 120 104" style="margin-top:24px"><path fill="#3d8fd4" d="M24 70a22 22 0 010-44 30 30 0 0158-8 24 24 0 0114 52z"/><path fill="#1a5fa8" d="M26 46l44-10 20 6v50l-44 10-20-6z"/><g stroke="#fff" stroke-width="3"><path d="M46 54v40M56 52v40M66 50v40M76 48v40"/></g></svg>
    <h3>Server Configuration</h3>
    <p>Lorem ipsum dolor sit amet, consectetur adipiscing elit. Curabitur lacinia pretium risus ac euismod.Arabitur lorem lacinia pretium risus ac ipsum dolor sit amet consectetur adi.</p>
    <span class="more">read more</span>
  </div>

  <div class="abs card" style="left:801px">
    <svg width="120" height="104" viewBox="0 0 120 104" style="margin-top:24px"><path fill="#4a97d8" d="M22 72a22 22 0 010-44 32 32 0 0160-8 26 26 0 0116 52z"/><rect x="36" y="56" width="50" height="44" rx="4" fill="#1a5fa8"/><path d="M44 56V44a17 17 0 0134 0v12" fill="none" stroke="#1a5fa8" stroke-width="7"/><circle cx="61" cy="74" r="6" fill="#fff"/><rect x="58" y="76" width="6" height="14" fill="#fff"/></svg>
    <h3>Security services</h3>
    <p>Lorem ipsum dolor sit amet, consectetur adipiscing elit. Curabitur lacinia pretium risus ac euismod.Arabitur lorem lacinia pretium risus ac ipsum dolor sit amet consectetur adi.</p>
    <span class="more">read more</span>
  </div>
</section>

<section>
  <h2 class="abs sec-title" style="left:83px;top:1341px;font-weight:400">WELCOME TO <b>KELVAR SYSTEMS</b></h2>
  <div class="abs rule" style="left:83px;top:1375px;width:1038px"></div>
  <div class="abs welcome-photo" role="img" aria-label="Smiling businessman holding a laptop and pointing at its screen"></div>
  <div class="abs welcome-text">
    <p>Kelvar Systems is an Adelaide based company with a single objective - to excel in the support and service of all computer and IT needs.</p>
    <p>We provide a high level of consulting services using the most experienced engineers at a reasonable and fair price. We believe in using a Business Value approach to every aspect of computer consulting to provide our clients with the most cost effective solutions.</p>
    <p>We strongly believe that we are in business with our clients. Each thing we do must be measured against our clients' business objectives. At the end of the day our client's success is our success.</p>
  </div>
</section>

<section class="abs partners"><span>Norvane</span><span>Castwell</span><span>Lumora</span><span>Quillnet</span><span>Brightpeak</span></section>

<footer class="abs footer">
  <h3 class="abs f-head" style="left:94px;top:56px;font-weight:400">LATEST EVENTS</h3>
  <div class="abs f-rule" style="left:94px;top:99px;width:402px"></div>
  <div class="abs event-thumb" style="left:97px;top:125px" role="img" aria-label="Hands writing notes beside a tablet"></div>
  <div class="abs event" style="top:122px"><h4>Article Title goes here</h4>Lorem ipsum dolor sit amet, consectetur adipiscing elit dolor sit amet sit amet, consectetur.<span class="rm">Read more +</span></div>
  <div class="abs f-rule" style="left:94px;top:244px;width:402px"></div>
  <div class="abs event-thumb" style="left:97px;top:268px" role="img" aria-label="Hands writing notes beside a tablet"></div>
  <div class="abs event" style="top:265px"><h4>Article Title goes here</h4>Lorem ipsum dolor sit amet, consectetur adipiscing elit dolor sit amet sit amet, consectetur.<span class="rm">Read more +</span></div>
  <div class="abs f-rule" style="left:94px;top:388px;width:402px"></div>

  <h3 class="abs f-head" style="left:574px;top:56px;font-weight:400">QUICKLINKS</h3>
  <div class="abs f-rule" style="left:574px;top:99px;width:206px"></div>
  <ul class="abs links" style="top:115px"><li>Home</li><li>Services</li><li>About us</li><li>Clients</li><li>Supports</li><li>Testimonials</li><li>Contact us</li></ul>
  <div class="abs f-rule" style="left:574px;top:339px;width:206px"></div>

  <h3 class="abs f-head" style="left:870px;top:56px;font-weight:400">QUICK MESSAGE</h3>
  <div class="abs f-rule" style="left:870px;top:99px;width:207px"></div>
  <p class="abs msg-intro" style="top:119px">Do you have Questions?<br>Message us today!</p>
  <div class="abs field" style="top:165px;height:30px">Firstname</div>
  <div class="abs field" style="top:207px;height:30px">Email Address</div>
  <div class="abs field" style="top:247px;height:78px">Message...</div>
  <div class="abs submit" style="top:333px">Submit</div>
</footer>

<div class="abs bar">
  <div class="abs bar-links">Sitemap | FAQ | Privacy Policy</div>
  <div class="abs bar-copy">Copyright 2014 · All rights reserved</div>
  <div class="abs bar-social"><span></span><span></span><span></span><span></span></div>
</div>
</body>
</html>
```